Cobalt Ridge Mini Storage - Ad for half Page

Need half page ad for a publication.
would also like to be able to use in the future
self storage facility - 3 locations, the third opening soon
do not like real busy projects...i have a logo but willing to tweak if needed

```html
<!DOCTYPE html>
<html lang="en">
<head>
<meta charset="utf-8">
<title>Cobalt Ridge Mini Storage – Half Page Ad</title>
<link href="https://fonts.googleapis.com/css2?family=Montserrat:wght@400;600;700;800;900&family=Rubik:wght@400;500&family=Dancing+Script:wght@600&display=swap" rel="stylesheet">
<style>
  :root {
    --backdrop: #4a4d50;
    --orange: #e89c0c;
    --brown: #4e1f05;
    --tan: #a87a50;
    --paper: #ffffff;
    --ink: #3a2415;
    --sky: #4fa6de;
  }
  * { margin: 0; padding: 0; box-sizing: border-box; }
  html, body { width: 1200px; height: 863px; overflow: hidden; background: var(--backdrop); }
  .page {
    position: absolute; left: 300px; top: 31px; width: 600px; height: 800px;
    background: var(--paper); overflow: hidden;
    font-family: "Rubik", sans-serif; color: var(--ink);
  }
  .page-top { position: absolute; inset: 0; }
  .photo-column { position: absolute; left: 0; top: 0; width: 600px; height: 800px; }
  .brand {
    position: absolute; left: 192px; top: 405px;
    display: flex; align-items: center; gap: 14px;
  }
  .brand-mark { width: 54px; height: 54px; background: var(--tan); }
  .brand-name {
    font-family: "Montserrat", sans-serif; font-weight: 800; color: var(--brown);
    font-size: 30px; line-height: 1.02; text-transform: uppercase; letter-spacing: .5px;
  }
  .tagline {
    position: absolute; left: 180px; width: 410px; top: 480px; text-align: center;
    font-family: "Montserrat", sans-serif; font-weight: 700; font-size: 12.5px; color: var(--brown);
  }
  .tagline .sep { color: var(--tan); margin: 0 4px; }
  .headline-band {
    position: absolute; left: 176px; top: 504px; width: 414px; height: 170px;
    background: var(--brown); color: var(--paper);
    font-family: "Montserrat", sans-serif; text-align: center; text-transform: uppercase;
    display: flex; flex-direction: column; justify-content: center;
  }
  .headline-band .line-light { font-weight: 400; font-size: 42px; line-height: 1; letter-spacing: 1px; }
  .headline-band .line-bold { font-weight: 900; font-size: 64px; line-height: 1; margin: 2px 0; }
  .locations {
    position: absolute; left: 180px; top: 688px; width: 412px;
    display: flex; gap: 8px;
  }
  .location {
    flex: 1; height: 84px; border: 1px solid var(--tan); position: relative;
    padding: 14px 6px 4px; font-size: 8.5px; line-height: 1.3; text-align: center;
  }
  .location .visit {
    position: absolute; top: -9px; left: 50%; transform: translateX(-50%);
    background: var(--paper); padding: 0 6px; white-space: nowrap;
    font-family: "Dancing Script", cursive; font-size: 12px; color: var(--ink);
  }
  .location .city { font-weight: 500; font-size: 9.5px; text-transform: uppercase; }
  .location .phone { font-weight: 500; font-size: 10px; display: inline-flex; align-items: center; gap: 3px; margin-top: 2px; }
  .location.soon { display: flex; align-items: center; justify-content: center; font-size: 10px; text-transform: uppercase; letter-spacing: .5px; }
  .website {
    position: absolute; left: 180px; top: 778px; width: 276px; text-align: center;
    font-family: "Montserrat", sans-serif; font-weight: 700; font-size: 13px; color: var(--brown);
  }
</style>
</head>
<body>
  <main class="page">
    <svg class="page-top" width="600" height="800" viewBox="0 0 600 800" aria-hidden="true">
      <path d="M0 0 H600 V372 C520 395 440 420 330 402 C250 390 200 370 0 360 Z" fill="var(--orange)"/>
    </svg>

    <svg class="photo-column" width="600" height="800" viewBox="0 0 600 800">
      <defs>
        <linearGradient id="units-photo" x1="0" y1="0" x2="0" y2="1">
          <stop offset="0" stop-color="#4fa6de"/><stop offset=".45" stop-color="#9b6a45"/><stop offset="1" stop-color="#d7c7b4"/>
        </linearGradient>
        <linearGradient id="office-photo" x1="0" y1="0" x2="0" y2="1">
          <stop offset="0" stop-color="#a9cbe6"/><stop offset=".5" stop-color="#8a6548"/><stop offset="1" stop-color="#d9d3ca"/>
        </linearGradient>
        <linearGradient id="building-photo" x1="0" y1="0" x2="0" y2="1">
          <stop offset="0" stop-color="#2f7ed0"/><stop offset=".55" stop-color="#8d8f92"/><stop offset="1" stop-color="#d6d3cf"/>
        </linearGradient>
      </defs>
      <path role="img" aria-label="Photo of a row of storage unit doors under a blue sky" d="M0 362 C60 362 120 366 172 372 V505 L0 520 Z" fill="url(#units-photo)"/>
      <path role="img" aria-label="Photo of the stone-faced leasing office entrance" d="M0 526 L172 511 V640 L0 655 Z" fill="url(#office-photo)"/>
      <path role="img" aria-label="Photo of a two-storey storage building with roll-up doors" d="M0 661 L172 646 V800 H0 Z" fill="url(#building-photo)"/>
    </svg>

    <div class="brand">
      <span class="brand-mark"></span>
      <span class="brand-name">Cobalt Ridge<br>Mini Storage</span>
    </div>

    <p class="tagline">Family-Owned<span class="sep">|</span>Discounts Available<span class="sep">|</span>Affordable Rates</p>

    <h1 class="headline-band">
      <span class="line-light">Need More</span>
      <span class="line-bold">Storage</span>
      <span class="line-light">Space?</span>
    </h1>

    <section class="locations">
      <div class="location">
        <span class="visit">Visit us in</span>
        <div class="city">Alder Springs</div>
        <div>Cobalt Ridge Mini Storage<br>4870 Ridgeline Pkwy<br>Alder Springs, TX 78401</div>
        <div class="phone">
          <svg width="8" height="8" viewBox="0 0 10 10" aria-hidden="true"><circle cx="5" cy="5" r="5" fill="var(--ink)"/><path d="M3 2.5 L4.2 3.7 L3.7 4.3 Q4.6 5.6 5.8 6.3 L6.4 5.8 L7.5 7 L6.8 7.6 Q4.5 7 2.6 3.3 Z" fill="#fff"/></svg>
          (555) 214-0386
        </div>
      </div>
      <div class="location">
        <span class="visit">Visit us in</span>
        <div class="city">Cedar Falls</div>
        <div>Cobalt Ridge Mini Storage<br>62 Orchard Ave Suite 4<br>Cedar Falls, TX 78522</div>
        <div class="phone">
          <svg width="8" height="8" viewBox="0 0 10 10" aria-hidden="true"><circle cx="5" cy="5" r="5" fill="var(--ink)"/><path d="M3 2.5 L4.2 3.7 L3.7 4.3 Q4.6 5.6 5.8 6.3 L6.4 5.8 L7.5 7 L6.8 7.6 Q4.5 7 2.6 3.3 Z" fill="#fff"/></svg>
          (555) 730-1942
        </div>
      </div>
      <div class="location soon">
        <span class="visit">Visit us in</span>
        <span>Opening<br>Soon</span>
      </div>
    </section>

    <p class="website">www.cobaltridgeministorage.com</p>
  </main>
</body>
</html>
```